TILVERA.COM is a premium domain sales company. Our competitors are companies like brankoport.com, selvatrix.com, quimbelstock.com. Our current site is at www.tilveras.com.

We want to have the ability to search for domains, to highlight special offers and have some testimonials on the index page.

The logo for the site is attached.

Please be sure that the order form fits on the screen without scrolling the page. I want the entire form, including the submit button to fit without any page scrolling.

Delivered product - INDEX PAGE, ORDER FORM AND CONTENT PAGE PSDs.

Target Market(s)

Small to Medium business professionals

Industry/Entity Type

It Company

Requirements
Must have
• 1. List of domains for sale
2. Simple search box with button to run the search
3. link for advanced search
4. testimonial area. Note - this can be a small box where a different testimonial is displayed on each page load.
Nice to have
• Would like the site to have some white space. Don't want a heavily packed website. Give it an "airy" feel.

```html
<!DOCTYPE html>
<html lang="en">
<head>
<meta charset="utf-8">
<title>TILVERA.COM – Premium Domains</title>
<link href="https://fonts.googleapis.com/css2?family=Oswald:wght@400;500&family=Open+Sans:wght@400;600;700&display=swap" rel="stylesheet">
<style>
:root{
  --bg:#e8e8e8;
  --white:#ffffff;
  --green:#3a9a2a;
  --green-dark:#1f6e1a;
  --green-light:#5fb83a;
  --blue:#1f67b0;
  --blue-dark:#16508c;
  --text:#333333;
  --muted:#666666;
  --row-alt:#eeeeee;
  --orange:#f7a21b;
  --footer:#2b2b2b;
  --red:#c0392b;
}
*{box-sizing:border-box;margin:0;padding:0}
html,body{width:1018px;height:1200px;overflow:hidden}
body{background:var(--bg);font-family:"Open Sans",sans-serif;color:var(--text);position:relative}
.abs{position:absolute}
.page{left:84px;top:0;width:848px;height:1124px;background:var(--white);box-shadow:0 0 6px rgba(0,0,0,.15)}
.brand{left:106px;top:26px;font-family:"Open Sans",sans-serif;font-weight:700;font-size:30px;color:var(--green-dark);letter-spacing:-.5px}
.help{left:726px;top:26px;font-family:"Oswald",sans-serif;font-size:13px;color:#555}
.help-phone{left:726px;top:48px;font-family:"Oswald",sans-serif;font-size:18px;color:var(--blue)}
.help-icon{left:694px;top:35px}
.nav{left:0;top:83px;width:1018px;height:48px;background:linear-gradient(#5aae32,#2f8a22 60%,#1f7419);border-bottom:1px solid #186014}
.nav a{position:absolute;top:14px;font-family:"Oswald",sans-serif;font-size:14px;color:var(--white);text-decoration:none}
.nav .divider{position:absolute;top:0;width:1px;height:48px;background:rgba(255,255,255,.35)}
.hero{left:84px;top:131px;width:848px;height:297px;background:radial-gradient(circle at 70% 40%,#3f8f2f,#1e5e1a 70%,#154a13)}
.hero-photo{left:98px;top:0;width:217px;height:297px;background:linear-gradient(#3f6f3a,#2a2a2a);opacity:.55}
.hero-title{left:403px;top:77px;font-family:"Oswald",sans-serif;font-size:24px;color:var(--white)}
.hero-rule{left:403px;top:105px;width:260px;height:1px;background:linear-gradient(90deg,rgba(255,255,255,.8),rgba(255,255,255,0))}
.hero-sub{left:404px;top:114px;font-family:"Oswald",sans-serif;font-size:13px;color:var(--white);font-weight:400}
.search-input{left:404px;top:147px;width:230px;height:38px;background:var(--white);border:none;border-radius:3px 0 0 3px}
.search-go{left:634px;top:147px;width:107px;height:38px;background:linear-gradient(#444,#111);color:var(--white);font-family:"Oswald",sans-serif;font-size:16px;text-align:center;line-height:38px;border-radius:0 3px 3px 0}
.hero-hint{left:409px;top:195px;font-size:10px;color:#e8f2e4}
.slide-arrow{top:244px;width:26px;height:43px;background:#f2f2f2;box-shadow:0 2px 2px rgba(0,0,0,.15)}
.tab{top:458px;height:37px;border-radius:6px 6px 0 0;color:var(--white);font-size:12px;text-align:center;line-height:37px;background:linear-gradient(#2d7bc6,var(--blue-dark))}
.tab.active{background:linear-gradient(#4aa52f,#2b8a22)}
.listing{left:100px;top:494px;width:567px;height:344px;background:linear-gradient(#45a12f,#1d7a25);border-radius:0 6px 6px 6px}
.listing-inner{left:17px;top:17px;width:533px;height:316px;background:var(--white);border-radius:6px;padding:5px 4px}
table{width:525px;border-collapse:collapse;font-size:11px}
th{background:var(--blue);color:var(--white);font-weight:600;font-size:12px;text-align:left;height:31px;padding-left:16px}
td{height:35px;padding-left:10px}
tbody tr:nth-child(even){background:var(--row-alt)}
.price{display:flex;align-items:center;gap:8px}
.buy{display:flex;align-items:center;gap:12px}
.adv{left:690px;top:457px;width:222px;height:318px;background:var(--green);border-radius:3px}
.adv-title{left:45px;top:12px;font-size:15px;font-weight:600;color:var(--white)}
.adv-body{left:10px;top:52px;width:202px;height:254px;background:linear-gradient(#fafafa,#fff);border-radius:40% 40% 0 0/12px 12px 0 0}
.lbl{position:absolute;font-size:10px;color:#555}
.field{position:absolute;height:22px;background:var(--white);border:1px solid #cfcfcf}
.chk{position:absolute;display:flex;align-items:center;gap:4px;font-size:9px;color:#555}
.box{width:10px;height:10px;border:1px solid #667;background:#fff;display:flex;align-items:center;justify-content:center}
.find-btn{position:absolute;left:61px;top:217px;width:129px;height:26px;border-radius:13px;background:linear-gradient(#ffc13a,#f08a0c);color:var(--white);font-weight:700;font-size:12px;text-align:center;line-height:26px}
.testi-head{left:694px;top:802px;font-family:"Oswald",sans-serif;font-size:18px;color:var(--blue)}
.testi-photo{left:700px;width:56px;height:60px;border:2px solid #ddd;background:linear-gradient(#c9b8a8,#7a6656)}
.testi-box{left:773px;width:145px;height:73px;background:#f7f7f7;border:1px solid #e0e0e0;font-size:9px;line-height:13.5px;padding:6px 9px;color:#444}
.testi-name{display:block;text-align:right;color:var(--red);margin-top:1px}
.promo{left:105px;top:863px;width:270px;height:217px;border:3px solid var(--blue);border-radius:4px;background:linear-gradient(135deg,#f4f1ec,#c8c2b8 70%,#444)}
.promo-title{left:9px;top:22px;font-size:19px;line-height:26px;color:#222}
.promo-tag{right:12px;bottom:8px;font-size:17px;color:var(--white)}
.safe{left:394px;top:862px;width:280px;height:219px;border:1px solid #ddd;background:linear-gradient(#fff,#f2f2f2);border-radius:3px}
.safe-title{left:26px;top:14px;font-size:17px;color:#222}
.safe-item{position:absolute;left:48px;font-size:11px;line-height:20px}
.safe-item b{display:block;font-weight:400;color:var(--green)}
.footer{left:0;top:1124px;width:1018px;height:76px;background:var(--footer);border-top:2px solid #555}
.badge{top:19px}
.social{top:12px;width:20px;height:20px;border-radius:2px}
.copy{right:102px;top:43px;font-size:10px;color:#ddd}
</style>
</head>
<body>
<div class="abs page"></div>

<header>
  <div class="abs brand">TILVERA.COM</div>
  <svg class="abs help-icon" width="26" height="22" viewBox="0 0 26 22"><path d="M4 3c2-2 4-1 5 1l1 3c0 1-1 2-2 3 1 3 3 5 6 6 1-1 2-2 3-2l3 1c2 1 3 3 1 5-3 3-9 1-13-3S1 6 4 3z" fill="#666"/></svg>
  <div class="abs help">Questions? We're here to help! Call today:</div>
  <div class="abs help-phone">03 5550 4821</div>
</header>

<nav class="abs nav">
  <a href="#" style="left:108px">HOME</a>
  <span class="divider" style="left:158px"></span>
  <a href="#" style="left:176px">CATEGORIES</a>
  <span class="divider" style="left:254px"></span>
  <a href="#" style="left:274px">FAQS</a>
  <span class="divider" style="left:315px"></span>
  <a href="#" style="left:337px">ABOUT US</a>
  <span class="divider" style="left:406px"></span>
  <a href="#" style="left:424px">CONTACT US</a>
  <svg class="abs" style="left:864px;top:14px" width="22" height="20" viewBox="0 0 22 20"><path d="M1 2h4l3 11h10l3-8H7" fill="none" stroke="#fff" stroke-width="1.6"/><circle cx="9" cy="17" r="1.6" fill="#fff"/><circle cx="17" cy="17" r="1.6" fill="#fff"/></svg>
  <a href="#" style="left:895px;top:16px;font-size:13px">Cart</a>
</nav>

<section class="abs hero">
  <div class="abs hero-photo" role="img" aria-label="Photo of a smiling businesswoman with arms crossed"></div>
  <h1 class="abs hero-title" style="font-weight:400">Find Your Domain</h1>
  <div class="abs hero-rule"></div>
  <p class="abs hero-sub">You can find the best name for your business...</p>
  <div class="abs search-input"></div>
  <div class="abs search-go">GO</div>
  <p class="abs hero-hint">Start your search by entering the first character of the domain name.</p>
</section>
<div class="abs slide-arrow" style="left:58px"><svg width="26" height="43"><path d="M16 12l-7 9 7 9" fill="none" stroke="#7cc23c" stroke-width="2"/></svg></div>
<div class="abs slide-arrow" style="left:932px"><svg width="26" height="43"><path d="M10 12l7 9-7 9" fill="none" stroke="#7cc23c" stroke-width="2"/></svg></div>

<div class="abs tab active" style="left:100px;width:136px">Featured Domains</div>
<div class="abs tab" style="left:242px;width:135px">Domain Categories</div>
<div class="abs tab" style="left:382px;width:135px">Daily Domain Deals</div>
<div class="abs tab" style="left:523px;width:135px">Value of Domain</div>

<section class="abs listing">
  <div class="abs listing-inner">
    <table>
      <thead><tr><th style="width:152px">Domain</th><th style="width:130px">Category</th><th style="width:135px">Price</th><th>Option</th></tr></thead>
      <tbody>
        <tr><td>GlowpathSigns.com</td><td>Contracts</td><td><span class="price"><svg width="14" height="14"><circle cx="5.5" cy="5.5" r="4" fill="none" stroke="#333" stroke-width="1.8"/><path d="M8.5 8.5l4 4" stroke="#333" stroke-width="2.2"/></svg>$9,400</span></td><td><span class="buy">Buy Now <svg width="8" height="8"><rect x=".5" y=".5" width="7" height="7" fill="none" stroke="#444"/><path d="M2 4h4M4 2l2 2-2 2" stroke="#444" fill="none"/></svg></span></td></tr>
        <tr><td>GlowpathSigns.com</td><td>Contracts</td><td><span class="price"><svg width="14" height="14"><circle cx="5.5" cy="5.5" r="4" fill="none" stroke="#333" stroke-width="1.8"/><path d="M8.5 8.5l4 4" stroke="#333" stroke-width="2.2"/></svg>$9,400</span></td><td><span class="buy">Buy Now <svg width="8" height="8"><rect x=".5" y=".5" width="7" height="7" fill="none" stroke="#444"/><path d="M2 4h4M4 2l2 2-2 2" stroke="#444" fill="none"/></svg></span></td></tr>
        <tr><td>GlowpathSigns.com</td><td>Contracts</td><td><span class="price"><svg width="14" height="14"><circle cx="5.5" cy="5.5" r="4" fill="none" stroke="#333" stroke-width="1.8"/><path d="M8.5 8.5l4 4" stroke="#333" stroke-width="2.2"/></svg>$9,400</span></td><td><span class="buy">Buy Now <svg width="8" height="8"><rect x=".5" y=".5" width="7" height="7" fill="none" stroke="#444"/><path d="M2 4h4M4 2l2 2-2 2" stroke="#444" fill="none"/></svg></span></td></tr>
        <tr><td>GlowpathSigns.com</td><td>Contracts</td><td><span class="price"><svg width="14" height="14"><circle cx="5.5" cy="5.5" r="4" fill="none" stroke="#333" stroke-width="1.8"/><path d="M8.5 8.5l4 4" stroke="#333" stroke-width="2.2"/></svg>$9,400</span></td><td><span class="buy">Buy Now <svg width="8" height="8"><rect x=".5" y=".5" width="7" height="7" fill="none" stroke="#444"/><path d="M2 4h4M4 2l2 2-2 2" stroke="#444" fill="none"/></svg></span></td></tr>
        <tr><td>GlowpathSigns.com</td><td>Contracts</td><td><span class="price"><svg width="14" height="14"><circle cx="5.5" cy="5.5" r="4" fill="none" stroke="#333" stroke-width="1.8"/><path d="M8.5 8.5l4 4" stroke="#333" stroke-width="2.2"/></svg>$9,400</span></td><td><span class="buy">Buy Now <svg width="8" height="8"><rect x=".5" y=".5" width="7" height="7" fill="none" stroke="#444"/><path d="M2 4h4M4 2l2 2-2 2" stroke="#444" fill="none"/></svg></span></td></tr>
        <tr><td>GlowpathSigns.com</td><td>Contracts</td><td><span class="price"><svg width="14" height="14"><circle cx="5.5" cy="5.5" r="4" fill="none" stroke="#333" stroke-width="1.8"/><path d="M8.5 8.5l4 4" stroke="#333" stroke-width="2.2"/></svg>$9,400</span></td><td><span class="buy">Buy Now <svg width="8" height="8"><rect x=".5" y=".5" width="7" height="7" fill="none" stroke="#444"/><path d="M2 4h4M4 2l2 2-2 2" stroke="#444" fill="none"/></svg></span></td></tr>
        <tr><td>GlowpathSigns.com</td><td>Contracts</td><td><span class="price"><svg width="14" height="14"><circle cx="5.5" cy="5.5" r="4" fill="none" stroke="#333" stroke-width="1.8"/><path d="M8.5 8.5l4 4" stroke="#333" stroke-width="2.2"/></svg>$9,400</span></td><td><span class="buy">Buy Now <svg width="8" height="8"><rect x=".5" y=".5" width="7" height="7" fill="none" stroke="#444"/><path d="M2 4h4M4 2l2 2-2 2" stroke="#444" fill="none"/></svg></span></td></tr>
        <tr><td>GlowpathSigns.com</td><td>Contracts</td><td><span class="price"><svg width="14" height="14"><circle cx="5.5" cy="5.5" r="4" fill="none" stroke="#333" stroke-width="1.8"/><path d="M8.5 8.5l4 4" stroke="#333" stroke-width="2.2"/></svg>$9,400</span></td><td><span class="buy">Buy Now <svg width="8" height="8"><rect x=".5" y=".5" width="7" height="7" fill="none" stroke="#444"/><path d="M2 4h4M4 2l2 2-2 2" stroke="#444" fill="none"/></svg></span></td></tr>
      </tbody>
    </table>
  </div>
</section>

<aside class="abs adv">
  <svg class="abs" style="left:28px;top:8px" width="30" height="30" viewBox="0 0 30 30"><circle cx="12" cy="12" r="9" fill="none" stroke="#fff" stroke-width="2.5"/><path d="M19 19l8 8" stroke="#fff" stroke-width="3.5" stroke-linecap="round"/></svg>
  <div class="abs adv-title">Advanced Search</div>
  <div class="abs adv-body">
    <span class="lbl" style="left:18px;top:20px">Keyword(s):</span>
    <span class="field" style="left:18px;top:36px;width:172px"></span>
    <span class="lbl" style="left:18px;top:80px">Extension:</span>
    <span class="chk" style="left:20px;top:99px"><span class="box"><svg width="8" height="8"><path d="M1 4l2 2 4-5" stroke="#335" fill="none"/></svg></span>All</span>
    <span class="chk" style="left:63px;top:99px"><span class="box"><svg width="8" height="8"><path d="M1 4l2 2 4-5" stroke="#335" fill="none"/></svg></span>.com</span>
    <span class="chk" style="left:115px;top:99px"><span class="box"><svg width="8" height="8"><path d="M1 4l2 2 4-5" stroke="#335" fill="none"/></svg></span>.net</span>
    <span class="chk" style="left:158px;top:99px"><span class="box"><svg width="8" height="8"><path d="M1 4l2 2 4-5" stroke="#335" fill="none"/></svg></span>.org</span>
    <span class="lbl" style="left:17px;top:144px">Price</span>
    <span class="field" style="left:52px;top:138px;width:58px"></span>
    <span class="lbl" style="left:118px;top:144px">To</span>
    <span class="field" style="left:136px;top:138px;width:54px"></span>
    <span class="lbl" style="left:12px;top:182px">Length</span>
    <span class="field" style="left:52px;top:176px;width:58px"></span>
    <span class="lbl" style="left:118px;top:182px">To</span>
    <span class="field" style="left:136px;top:176px;width:54px"></span>
    <div class="find-btn">Find Domain</div>
  </div>
</aside>

<h2 class="abs testi-head" style="font-weight:400">TESTIMONIALS</h2>
<div class="abs testi-photo" style="top:838px" role="img" aria-label="Portrait photo of customer Mary"></div>
<div class="abs testi-box" style="top:835px">Uenim ad minim veniam, quis laboris nisi utaliquip ex irur dolor into Uenim ad minim veniam,<span class="testi-name">Mary</span></div>
<div class="abs testi-photo" style="top:924px" role="img" aria-label="Portrait photo of customer Mary"></div>
<div class="abs testi-box" style="top:921px">Uenim ad minim veniam, quis laboris nisi utaliquip ex irur dolor into Uenim ad minim veniam,<span class="testi-name">Mary</span></div>
<div class="abs testi-photo" style="top:1010px" role="img" aria-label="Portrait photo of customer John"></div>
<div class="abs testi-box" style="top:1007px">Uenim ad minim veniam, quis laboris nisi utaliquip ex irur dolor into Uenim ad minim veniam,<span class="testi-name">John</span></div>

<section class="abs promo" role="img" aria-label="Photo of a businesswoman giving a thumbs up beside a laptop">
  <div class="abs promo-title">Get Your Domain<br>Name Today,</div>
  <div class="abs promo-tag">We make it Easy!</div>
</section>

<section class="abs safe">
  <div class="abs safe-title">Safe and Secure</div>
  <svg class="abs" style="left:20px;top:58px" width="26" height="22" viewBox="0 0 26 22"><path d="M2 12l7 7L24 3" fill="none" stroke="#2ea02a" stroke-width="4" stroke-linecap="round"/></svg>
  <div class="safe-item" style="top:59px"><b>Service you can trust</b>Servicing thousands of clients since 2005.</div>
  <svg class="abs" style="left:21px;top:110px" width="22" height="22" viewBox="0 0 22 22"><path d="M11 1l3 7 7 .5-5.5 4.5 2 7L11 16l-6.5 4 2-7L1 8.5 8 8z" fill="#f59a12"/></svg>
  <div class="safe-item" style="top:110px"><b>100% Satisfaction Guaranteed</b>Your satisfaction is our priority!</div>
  <svg class="abs" style="left:22px;top:168px" width="22" height="22" viewBox="0 0 22 22"><circle cx="11" cy="11" r="9" fill="none" stroke="#d33" stroke-width="4" stroke-dasharray="7 7"/><circle cx="11" cy="11" r="9" fill="none" stroke="#eee" stroke-width="4" stroke-dasharray="7 7" stroke-dashoffset="7"/></svg>
  <div class="safe-item" style="top:163px"><b>Support Center</b>Have a question or comment?</div>
</section>

<footer class="abs footer">
  <div class="abs badge" style="left:89px;width:68px;height:32px;border-radius:16px;background:#f4f4f4" role="img" aria-label="Security certificate badge"></div>
  <div class="abs badge" style="left:173px;top:17px;width:26px;height:36px;background:#1f5fa0" role="img" aria-label="Business accreditation badge"></div>
  <div class="abs badge" style="left:220px;top:18px;width:31px;height:31px;border-radius:50%;background:#b52020" role="img" aria-label="Money back guarantee seal"></div>
  <div class="abs social" style="left:797px;background:#3b5a9a" role="img" aria-label="Social network link"></div>
  <div class="abs social" style="left:828px;background:#2a9fd8" role="img" aria-label="Social network link"></div>
  <div class="abs social" style="left:860px;background:#1e75b0" role="img" aria-label="Social network link"></div>
  <div class="abs social" style="left:893px;background:#f28a1a" role="img" aria-label="News feed link"></div>
  <div class="abs copy">© 2013 tilveras.com., All Rights Reserved</div>
</footer>
</body>
</html>
```